Copper Lantern - responsive bootstrap website design

Looking to build a responsive service website.

Logo has been provided.

PLEASE REVIEW ATTACHED DESIGN STYLE GUIDES & CLIENT CREATIVE BRIEF FOR OUR REQUIREMENT.

THANK YOU AND GOOD LUCK!

Industry/Entity Type

Build

```html
<!DOCTYPE html>
<html lang="en">
<head>
<meta charset="utf-8">
<title>Copper Lantern Outfitters</title>
<link href="https://fonts.googleapis.com/css2?family=Mulish:wght@400;600;700&family=Open+Sans:wght@400;600&display=swap" rel="stylesheet">
<style>
:root{
  --black:#000;
  --nav-top:#1d5f95;
  --nav-bottom:#083a66;
  --navy:#0b2a4a;
  --ink:#222;
  --body:#666;
  --muted:#888;
  --blue-title:#1d5b8f;
  --link:#1f6fb0;
  --orange:#d9731a;
  --grey-bg:#f7f7f7;
  --line:#e4e4e4;
  --brown:#7a5238;
  --fb:#3d5ea8;
  --tw:#3ab3e0;
}
*{box-sizing:border-box;margin:0;padding:0}
html,body{width:712px;height:1200px;overflow:hidden;background:#fff}
body{position:relative;font-family:"Open Sans",Arial,sans-serif;color:var(--body)}
.abs{position:absolute}
.site-header{left:0;top:0;width:712px;height:80px;background:var(--black)}
.brand{left:0;top:18px;width:712px;text-align:center;color:#fff;font-family:"Mulish",Arial,sans-serif;font-weight:400;font-size:20px;line-height:22px}
.brand .sub{display:block;font-size:16px}
.main-nav{left:0;top:80px;width:712px;height:34px;background:linear-gradient(var(--nav-top),var(--nav-bottom));display:flex;justify-content:center}
.main-nav a{color:#fff;text-decoration:none;font-family:"Mulish",Arial,sans-serif;font-weight:600;font-size:9px;line-height:34px;padding:0 13.5px;border-right:1px solid rgba(0,0,0,.35)}
.main-nav a:last-child{border-right:0}
.hero{left:0;top:114px;width:712px;height:295px;background:linear-gradient(100deg,#8fa0ac 0%,#c9cfd3 40%,#6e7c84 70%,#495a64 100%)}
.hero-arrow{top:228px}
h2{font-family:"Mulish",Arial,sans-serif;font-weight:400}
.welcome-title{left:67px;top:443px;font-size:18px;color:var(--ink)}
.welcome-text{left:67px;top:471px;width:352px;font-size:7.3px;line-height:12.3px}
.welcome-text p+p{margin-top:7px}
.section-title{font-size:15px}
.title-blue{color:var(--blue-title)}
.title-orange{color:var(--orange)}
.title-dark{color:var(--ink)}
.thumb-grid{display:grid;grid-template-columns:repeat(3,60px);gap:4px}
.thumb{height:47px;background:linear-gradient(135deg,#4f7ea6,#b9c7d2);position:relative}
.thumb.alt{background:linear-gradient(135deg,#3c6b8d,#2a3c4c)}
.thumb.green{background:linear-gradient(135deg,#5c7a3a,#8aa05a)}
.play{position:absolute;left:23px;top:16px;width:14px;height:14px;border-radius:50%;background:rgba(0,0,0,.75);border:1px solid #fff}
.play::after{content:"";position:absolute;left:5px;top:3.5px;border-left:5px solid #fff;border-top:3px solid transparent;border-bottom:3px solid transparent}
.band{left:0;top:603px;width:712px;height:238px;background:var(--grey-bg);border-top:1px solid #efefef;border-bottom:1px solid #efefef}
.blog-item{display:flex;gap:9px;margin-bottom:16px}
.blog-thumb{width:44px;height:38px;flex:none;background:linear-gradient(#6b9bc6,#2f5f8a)}
.blog-item h3,.news-item h3{font-family:"Open Sans",Arial,sans-serif;font-weight:400;font-size:8.3px;color:var(--ink);line-height:12px}
.blog-item p,.news-item p{font-size:6.8px;line-height:10.5px;color:var(--body)}
.time{font-size:7.2px;color:var(--link)}
.news-item{margin-bottom:12px}
.news-item h3{color:var(--link);font-size:8.8px;margin-bottom:3px}
.feed{top:886px;width:179px;height:215px;border:1px solid var(--line);background:#fff}
.feed-head{height:28px;color:#fff;font-family:"Mulish",Arial,sans-serif;font-size:11.5px;line-height:28px;padding-left:13px;position:relative}
.feed-head .dot{position:absolute;right:11px;top:6px;width:16px;height:16px;border-radius:50%;background:#fff}
.feed-head.square .dot{border-radius:2px}
.head-brown{background:var(--brown)}
.head-fb{background:var(--fb)}
.head-tw{background:var(--tw)}
.feed-body{padding:10px 8px 0 9px}
.post{display:flex;gap:8px;margin-bottom:11px}
.avatar{width:30px;height:29px;flex:none;background:linear-gradient(#c9b29b,#8c7462)}
.post h4{font-family:"Open Sans",Arial,sans-serif;font-weight:400;font-size:7.8px;color:var(--ink);line-height:11px}
.post p{font-size:6.4px;line-height:9.6px;color:var(--muted)}
.post .stamp{font-size:6.6px;color:#444;margin-top:4px}
.tweet{margin:0 0 10px 7px}
.tweet h4{font-family:"Open Sans",Arial,sans-serif;font-weight:400;font-size:7.4px;color:var(--ink);line-height:11px}
.tweet h4 span{color:var(--tw);font-size:6.6px}
.tweet p{font-size:6.4px;line-height:9.6px;color:var(--muted)}
.tweet .stamp{font-size:6.6px;color:#444;margin-top:2px;display:flex;align-items:center;gap:4px}
.site-footer{left:0;top:1130px;width:712px;height:70px;background:var(--navy)}
.footer-nav{left:68px;top:1150px;font-family:"Mulish",Arial,sans-serif;font-weight:700;font-size:8.2px;color:#fff;word-spacing:1px}
.copyright{left:68px;top:1167px;font-size:6.8px;color:#8a9bb0}
.social{left:574px;top:1145px;display:flex;gap:2px}
.social span{width:16px;height:16px;border-radius:50%;background:#fff}
</style>
</head>
<body>
<header class="site-header abs">
  <div class="brand abs">Copper Lantern<span class="sub">Outfitters</span></div>
</header>
<nav class="main-nav abs">
  <a href="#">HOME</a><a href="#">ABOUT US</a><a href="#">GUIDE SERVICES</a><a href="#">MERCHANDISE</a><a href="#">VIDEO</a><a href="#">PHOTO GALLERY</a><a href="#">CONTACT</a>
</nav>
<div class="hero abs" role="img" aria-label="Smiling angler in an orange jacket holding a large halibut by the water"></div>
<svg class="hero-arrow abs" style="left:14px" width="24" height="44" viewBox="0 0 24 44"><polyline points="22,2 2,22 22,42" fill="none" stroke="#1a2f45" stroke-width="1.8"/></svg>
<svg class="hero-arrow abs" style="left:672px" width="24" height="44" viewBox="0 0 24 44"><polyline points="2,2 22,22 2,42" fill="none" stroke="#1a2f45" stroke-width="1.8"/></svg>

<h2 class="welcome-title abs">Welcome to Copper Lantern Outfitters</h2>
<div class="welcome-text abs">
  <p>Lowcountry’s own Copper Lantern Outfitters is your ultimate destination for saltwater fishing. From fly fishing for tailing reds in a foot of water to chasing Pelagic in the Gulf Stream, here you’ll find all the gear, apparel, and expert advice you’ll need to make the most of your time on the water.</p>
  <p>Looking for guidance? Copper Lantern Outfitters provides professional guide services featuring the areas’ best captains and crews. Regardless of your skill level or experience, we can accommodate your group to create an exhilarating and memorable fishing experience.</p>
</div>

<h2 class="section-title title-blue abs" style="left:455px;top:443px">Video Gallery</h2>
<div class="thumb-grid abs" style="left:458px;top:469px" role="img" aria-label="Video thumbnails of fishing trips">
  <div class="thumb"><span class="play"></span></div><div class="thumb alt"><span class="play"></span></div><div class="thumb green"><span class="play"></span></div>
  <div class="thumb alt"><span class="play"></span></div><div class="thumb"><span class="play"></span></div><div class="thumb alt"><span class="play"></span></div>
</div>

<div class="band abs"></div>
<h2 class="section-title title-dark abs" style="left:67px;top:630px">Recent Blog</h2>
<div class="abs" style="left:67px;top:656px;width:180px">
  <div class="blog-item"><div class="blog-thumb" role="img" aria-label="Fishing boat at the dock"></div><div><h3>Morbi eget arcu</h3><p>Vivamus porttitor g purus nisi eleif-end libero a tempus Ut nisi erat</p><span class="time">2 hous ago</span></div></div>
  <div class="blog-item"><div class="blog-thumb" role="img" aria-label="Sky over open water"></div><div><h3>Curabitur iaculis</h3><p>Vivamus porttitor g purus nisi eleif-end libero a tempus Ut nisi erat</p><span class="time">2 hous ago</span></div></div>
  <div class="blog-item"><div class="blog-thumb" role="img" aria-label="Fishing rod over the sea"></div><div><h3>Curabitur iaculis</h3><p>Vivamus porttitor g purus nisi eleif-end libero a tempus</p><span class="time">2 hous ago</span></div></div>
</div>

<h2 class="section-title title-orange abs" style="left:265px;top:630px">Latest News</h2>
<div class="abs" style="left:266px;top:654px;width:172px">
  <div class="news-item"><h3>Donec scelerisque leo ac</h3><p>Etiam nulla massa pharetra facilisis volutpat in imperdiet sit amet sem Aliquam nec erat</p></div>
  <div class="news-item"><h3>Class aptent taciti sociosqu</h3><p>Etiam nulla massa pharetra facilisis volutpat in imperdiet sit amet sem</p></div>
  <div class="news-item"><h3>Vivamus porttitor purus nisi</h3><p>Donec scelerisque leo ac risus Praesent sit amet est In dictum dolor eu dictum porttitor enim felis viverra mi eget luctus massa purus</p></div>
</div>

<h2 class="section-title title-blue abs" style="left:456px;top:630px">Photo Gallery</h2>
<div class="thumb-grid abs" style="left:458px;top:658px" role="img" aria-label="Photos of anglers, boats and catches">
  <div class="thumb alt"></div><div class="thumb"></div><div class="thumb"></div>
  <div class="thumb"></div><div class="thumb green"></div><div class="thumb green"></div>
  <div class="thumb"></div><div class="thumb alt"></div><div class="thumb green"></div>
</div>

<section class="feed abs" style="left:70px">
  <div class="feed-head head-brown square">Photo Stream<span class="dot"></span></div>
  <div class="feed-body">
    <div class="post"><div class="avatar" role="img" aria-label="Member portrait"></div><div><h4>Etiam eu urna</h4><p>Nulla sit amet diam Duis non nunc libero a tempus libero lectus feugiat felis Morbi diam mauris viverra in gravida eu mattis in ante Morbi eget arcu Morbi porta libero id ullamcorper nonummy nibh ligula pulvinar metus</p><p class="stamp">Posted 2 hours ago</p></div></div>
    <div class="post"><div class="avatar" role="img" aria-label="Member portrait"></div><div><h4>Donec convallis pede</h4><p>Mauris vel lacus vitae felis vestibulum volutpat Etiam est nunc venenatis in tristique eu imperdiet ac nisl Cum sociis natoque penatibus</p><p class="stamp">Posted 2 hours ago</p></div></div>
  </div>
</section>
<section class="feed abs" style="left:266px">
  <div class="feed-head head-fb">Community Feed<span class="dot"></span></div>
  <div class="feed-body">
    <div class="post"><div class="avatar" role="img" aria-label="Member portrait"></div><div><h4>Etiam eu urna</h4><p>Malesuada nec ultricies sit amet porttitor mattis enim In massa libero inter</p><p class="stamp">Posted 2 hours ago</p></div></div>
    <div class="post"><div class="avatar" role="img" aria-label="Member portrait"></div><div><h4>Nulla sit amet diam</h4><p>Malesuada nec ultricies sit amet porttit-mattis enim In massa libero interdu</p><p class="stamp">Posted 2 hours ago</p></div></div>
    <div class="post"><div class="avatar" role="img" aria-label="Member portrait"></div><div><h4>Donec convallis pede</h4><p>Malesuada nec ultricies sit amet porttitor mattis enim In massa libero interdum nec interdum vel blandit sed</p><p class="stamp">Posted 2 hours ago</p></div></div>
  </div>
</section>
<section class="feed abs" style="left:464px">
  <div class="feed-head head-tw">Chatter Feed<span class="dot"></span></div>
  <div class="feed-body">
    <div class="tweet"><h4>Etiam eu urna @ <span>Etiam eu urna</span></h4><p>Malesuada nec ultricies sit amet porttitor mattis enim In massa libero interdu</p><p class="stamp">Posted 2 hours ago <svg width="9" height="7" viewBox="0 0 9 7"><path d="M0 5 Q4 7 8 1 L6 1 Q3 4 0 5Z" fill="#555"/></svg></p></div>
    <div class="tweet"><h4>Donec convallis pede @ <span>Vivamus sollicitu-</span></h4><p>Malesuada nec ultricies sit amet porttitor mattis enim In massa libero interdu</p><p class="stamp">Posted 2 hours ago <svg width="9" height="7" viewBox="0 0 9 7"><path d="M0 5 Q4 7 8 1 L6 1 Q3 4 0 5Z" fill="#555"/></svg></p></div>
    <div class="tweet"><h4>Aliquam erat @ <span>Donec scelerisque leo</span></h4><p>Vestibulum gravida Praesent elementum elit at tellus Malesuada nec ultricies sit amet porttitor mattis enim In massa libero interdum</p><p class="stamp">Posted 2 hours ago <svg width="9" height="7" viewBox="0 0 9 7"><path d="M0 5 Q4 7 8 1 L6 1 Q3 4 0 5Z" fill="#555"/></svg></p></div>
  </div>
</section>

<footer class="site-footer abs"></footer>
<div class="footer-nav abs">HOME | ABOUT US | GUIDE SERVICES | MERCHANDISE | VIDEO | PHOTO GALLERY | CONTACT</div>
<div class="copyright abs">© 2014 Company Name &nbsp;All right reserved &nbsp;Term of Use</div>
<div class="social abs"><span></span><span></span><span></span><span></span></div>
</body>
</html>
```